Harlow Ridge Growers and Nursery needs a business street sign.

I have three businesses located at the same address: The Harlow Ridge Growers & Nursery, The Bramble Nook, and The Quarry Commons. I am looking for a 4’ x 8’ street sign to represent all three businesses as one retail experience. It needs to be eye catching yet simple enough that people can fully read it while driving by. I have logos for the greenhouse and village however I do not have anything for The Bramble Nook. I’m looking for some type of font that’s similar or in between the two attached logos for The Bramble Nook.

• Horizontal Sign, Eye catching, yet simple design so people see it while driving by.
• Horizontal Sign
• I’m open to the design being both vertical and horizontal. Please provide both options

```html
<!DOCTYPE html>
<html lang="en">
<head>
<meta charset="utf-8">
<title>Harlow Ridge Growers &amp; Nursery — Street Sign</title>
<link rel="stylesheet" href="https://fonts.googleapis.com/css2?family=Josefin+Sans:wght@700&family=Oswald:wght@500&display=swap">
<style>
  :root {
    --green: #126b3d;
    --maroon: #6e2b2b;
    --panel: #ececec;
    --cream: #f1e4c8;
    --magenta: #a3155f;
    --page: #ffffff;
  }
  html, body {
    margin: 0;
    width: 881px;
    height: 1200px;
    overflow: hidden;
    background: var(--page);
  }
  .street-sign {
    position: absolute;
    left: 20px;
    top: 390px;
    width: 841px;
    height: 420px;
    display: block;
  }
  .brand-name { font-family: "Josefin Sans", sans-serif; font-weight: 700; }
  .tagline { font-family: "Josefin Sans", sans-serif; font-weight: 700; fill: var(--cream); }
  .phone { font-family: "Oswald", sans-serif; font-weight: 500; fill: var(--maroon); }
  .contact { font-family: "Oswald", sans-serif; font-weight: 500; fill: var(--cream); font-size: 25px; }
</style>
</head>
<body>
<svg class="street-sign" viewBox="0 0 1440 720" role="img" aria-label="Street sign for Harlow Ridge Growers &amp; Nursery, Quarry Commons and Bramble Nook">
  <!-- panel -->
  <rect class="sign-panel" x="0" y="0" width="1440" height="720" fill="var(--panel)"/>

  <!-- top band -->
  <polygon class="top-band" points="0,0 1440,0 1440,58 0,55" fill="var(--green)"/>
  <polygon class="top-rule" points="0,55 1440,58 1440,75 0,70" fill="var(--maroon)"/>

  <!-- bottom band -->
  <polygon class="bottom-rule" points="0,645 1440,660 1440,668 0,663" fill="var(--maroon)"/>
  <polygon class="bottom-band" points="0,663 1440,668 1440,720 0,720" fill="var(--green)"/>

  <!-- slanted divider -->
  <polygon class="divider-edge" points="952,68 964,68 884,656 872,656" fill="var(--maroon)"/>
  <polygon class="divider" points="964,68 1022,70 938,657 884,656" fill="var(--green)"/>

  <!-- right divider -->
  <polygon class="right-rule" points="985,333 1440,333 1440,345 983,345" fill="var(--maroon)"/>
  <polygon class="right-band" points="983,345 1440,345 1440,385 978,385" fill="var(--green)"/>

  <!-- main business -->
  <text class="brand-name" x="60" y="200" font-size="70" fill="var(--green)">The</text>
  <text class="brand-name" x="60" y="335" font-size="128" fill="var(--green)" textLength="800" lengthAdjust="spacingAndGlyphs">Harlow Ridge</text>

  <rect class="tagline-bar" x="200" y="395" width="660" height="70" rx="14" fill="var(--maroon)" stroke="var(--green)" stroke-width="4"/>
  <text class="tagline" x="530" y="447" font-size="44" text-anchor="middle">GROWERS &amp; NURSERY</text>

  <text class="phone" x="532" y="580" font-size="118" text-anchor="middle" textLength="620" lengthAdjust="spacingAndGlyphs">555-014-1350</text>

  <!-- Quarry Commons -->
  <text class="brand-name" x="1228" y="170" font-size="66" fill="var(--maroon)" text-anchor="middle">Quarry</text>
  <text class="brand-name" x="1228" y="228" font-size="50" fill="var(--maroon)" text-anchor="middle">Commons</text>
  <text class="phone" x="1228" y="300" font-size="62" text-anchor="middle" textLength="310" lengthAdjust="spacingAndGlyphs">555-014-3750</text>

  <!-- Bramble Nook -->
  <text class="brand-name" x="1215" y="520" font-size="86" fill="var(--magenta)" text-anchor="middle">Bramble</text>
  <text class="brand-name" x="1215" y="585" font-size="56" fill="var(--magenta)" text-anchor="middle">Nook</text>
  <text class="phone" x="1190" y="650" font-size="62" text-anchor="middle" textLength="300" lengthAdjust="spacingAndGlyphs">555-014-2112</text>

  <!-- contact strip -->
  <g class="icon-mail">
    <circle cx="108" cy="692" r="12" fill="var(--cream)"/>
    <rect x="100" y="687" width="16" height="10" fill="var(--green)"/>
    <polyline points="100,687 108,693 116,687" fill="none" stroke="var(--cream)" stroke-width="1.5"/>
  </g>
  <text class="contact" x="126" y="701">INFO@HARLOWRIDGEGROWERS.NET</text>

  <g class="icon-web" fill="none" stroke="var(--cream)" stroke-width="2">
    <circle cx="578" cy="692" r="11"/>
    <ellipse cx="578" cy="692" rx="5" ry="11"/>
    <line x1="567" y1="692" x2="589" y2="692"/>
  </g>
  <text class="contact" x="594" y="701">HARLOWRIDGEGROWERS.NET</text>

  <path class="icon-pin" d="M960,704 C953,695 950,690 950,685 a10,10 0 0 1 20,0 C970,690 967,695 960,704 Z M960,681 a4,4 0 1 0 0.01,0 Z" fill="var(--cream)" fill-rule="evenodd"/>
  <text class="contact" x="974" y="701">2740 NORTH ROUTE 12 ASHBY, NJ 08390</text>
</svg>
</body>
</html>
```